Lark Ridge Property Biz Card
Business card and stationary
Project: Lark Ridge Property Biz Card
Lark Ridge Property Biz Card - Real Estate
Creative Brief
Professional
Dwight Fenmore
DO NOT ADD AN ADDRESS
dfenmore@larkridgeproperty.com
On the front I would like the logo, my name, phone number and email address. Also please have the catch phrase: "We buy houses, any condition! Get Cash Fast! Quick Closing!" The colour scheme of my logo is not set in stone, so please feel free to experiment with the colours.
On the back of the card please have the company logo

```html
<!DOCTYPE html>
<html lang="en">
<head>
<meta charset="utf-8">
<title>Lark Ridge Property – Stationery Set</title>
<link href="https://fonts.googleapis.com/css2?family=Roboto+Condensed:wght@400;700&display=swap" rel="stylesheet">
<style>
  :root{
    --stage:#3b3b3d;
    --paper:#ffffff;
    --navy:#1f4a7e;
    --navy-dark:#173a64;
    --slate:#6d6f73;
    --ink:#3c3f44;
    --ghost:rgba(31,74,126,0.07);
  }
  *{box-sizing:border-box;margin:0;padding:0}
  html,body{width:1200px;height:346px;overflow:hidden;background:var(--stage)}
  body{position:relative;font-family:"Roboto Condensed",Arial,sans-serif;color:var(--ink)}
  .item{position:absolute;background:var(--paper);box-shadow:0 3px 8px rgba(0,0,0,.45);overflow:hidden}

  .brand{display:flex;flex-direction:column;align-items:center;gap:2px;color:var(--navy);font-weight:700;text-transform:uppercase;line-height:1;text-align:center}
  .brand-mark{background:currentColor}
  .brand-name{letter-spacing:.04em}

  /* business cards */
  .card{left:19px;width:135px;height:70px}
  .card-front{top:88px}
  .card-front .brand{position:absolute;left:8px;top:12px;font-size:7px}
  .card-front .brand-mark{width:12px;height:12px}
  .card-front .brand-name{width:40px}
  .card-details{position:absolute;left:62px;top:12px;font-size:4.5px;line-height:1.45;color:var(--ink)}
  .card-details .person{font-size:6px;font-weight:700;color:var(--navy)}
  .card-tagline{position:absolute;left:8px;bottom:6px;font-size:4px;color:var(--slate)}
  .card-back{top:164px;height:60px}
  .card-back .brand{position:absolute;inset:0;justify-content:center;font-size:7px}
  .card-back .brand-mark{width:13px;height:13px}
  .card-blue{top:230px;height:66px;background:var(--navy)}
  .card-blue .brand{position:absolute;left:0;right:0;top:16px;color:#fff;font-size:7px}
  .card-blue .brand-mark{width:12px;height:12px}
  .card-blue .web{position:absolute;left:0;right:0;bottom:8px;text-align:center;font-size:4.5px;color:#d6e0ec}

  /* letterheads */
  .letter{top:24px;width:221px;height:302px;border-left:4px solid var(--navy)}
  .letter-a{left:163px}
  .letter-b{left:403px}
  .letter .brand{position:absolute;left:18px;top:14px;font-size:8px}
  .letter .brand-mark{width:14px;height:14px}
  .letter-b .brand{left:0;right:0}
  .letter-contact{position:absolute;left:100px;top:16px;font-size:4.5px;line-height:1.5;color:var(--slate)}
  .letter-ghost{position:absolute;left:50%;top:52%;transform:translate(-50%,-50%);width:90px;height:90px;background:var(--ghost)}
  .letter-footer{position:absolute;left:14px;right:10px;bottom:9px;font-size:4.5px;color:var(--slate);text-align:center}

  /* small envelopes */
  .env{width:163px;height:100px}
  .env-a{left:643px;top:70px}
  .env-b{left:643px;top:202px}
  .env .brand{position:absolute;left:10px;top:10px;font-size:6px}
  .env .brand-mark{width:10px;height:10px}
  .env-line{position:absolute;left:10px;bottom:12px;font-size:4px;color:var(--slate)}

  /* long envelopes */
  .long{left:895px;width:280px;height:98px}
  .long-gray{top:20px;background:#e9eaec}
  .long-blue{top:98px;background:var(--navy)}
  .long-white{top:182px;height:118px}
  .long svg{position:absolute;inset:0}
  .long .brand{position:absolute;left:0;right:0;font-size:6px}
  .long .brand-mark{width:10px;height:10px}
  .long-gray .brand{top:28px}
  .long-white .brand{top:44px}
  .long-blue .brand{left:14px;right:auto;top:12px;color:#fff}
</style>
</head>
<body>

<section class="item card card-front" aria-label="Business card front">
  <div class="brand"><span class="brand-mark"></span><span class="brand-name">Lark Ridge Property</span></div>
  <div class="card-details">
    <div class="person">Dwight Fenmore</div>
    <div>Acquisitions Manager</div>
    <div>(204) 555-0148</div>
    <div>dfenmore@larkridgeproperty.com</div>
    <div>Skype: mosslane77</div>
  </div>
  <div class="card-tagline">We buy houses, any condition! Get Cash Fast! Quick Closing!</div>
</section>

<section class="item card card-back" aria-label="Business card back">
  <div class="brand"><span class="brand-mark"></span><span class="brand-name">Lark Ridge Property</span></div>
</section>

<section class="item card card-blue" aria-label="Business card back, blue">
  <div class="brand"><span class="brand-mark"></span><span class="brand-name">Lark Ridge Property</span></div>
  <div class="web">www.larkridgeproperty.com</div>
</section>

<section class="item letter letter-a" aria-label="Letterhead">
  <div class="brand"><span class="brand-mark"></span><span class="brand-name">Lark Ridge Property</span></div>
  <div class="letter-contact">
    <div>(204) 555-0148</div>
    <div>dfenmore@larkridgeproperty.com</div>
    <div>www.larkridgeproperty.com</div>
  </div>
  <div class="letter-ghost"></div>
  <div class="letter-footer">We buy houses, any condition! Get Cash Fast! Quick Closing!</div>
</section>

<section class="item letter letter-b" aria-label="Continuation sheet">
  <div class="brand"><span class="brand-mark"></span><span class="brand-name">Lark Ridge Property</span></div>
  <div class="letter-ghost"></div>
  <div class="letter-footer">(204) 555-0148 · dfenmore@larkridgeproperty.com · www.larkridgeproperty.com</div>
</section>

<section class="item env env-a" aria-label="Envelope front">
  <div class="brand"><span class="brand-mark"></span><span class="brand-name">Lark Ridge Property</span></div>
  <div class="env-line">www.larkridgeproperty.com</div>
</section>

<section class="item env env-b" aria-label="Envelope front">
  <div class="brand"><span class="brand-mark"></span><span class="brand-name">Lark Ridge Property</span></div>
  <div class="env-line">www.larkridgeproperty.com</div>
</section>

<section class="item long long-gray" aria-label="Envelope back, gray flap">
  <svg width="280" height="98" viewBox="0 0 280 98"><polygon points="0,0 280,0 140,58" fill="#6f7175"/></svg>
  <div class="brand"><span class="brand-mark"></span><span class="brand-name">Lark Ridge Property</span></div>
</section>

<section class="item long long-blue" aria-label="Envelope back, blue flap">
  <svg width="280" height="98" viewBox="0 0 280 98"><polygon points="0,98 0,40 140,72 280,40 280,98" fill="#ffffff"/></svg>
  <div class="brand"><span class="brand-mark"></span><span class="brand-name">Lark Ridge Property</span></div>
</section>

<section class="item long long-white" aria-label="Envelope back, white">
  <svg width="280" height="118" viewBox="0 0 280 118"><polyline points="0,0 140,62 280,0" fill="none" stroke="#c9ccd1" stroke-width="1"/><polyline points="0,118 120,58 M280,118 160,58" fill="none" stroke="#dfe1e4" stroke-width="1"/></svg>
  <div class="brand"><span class="brand-mark"></span><span class="brand-name">Lark Ridge Property</span></div>
</section>

</body>
</html>
```